New Coffee Shop business card

We are opening our new coffee shop and are needing business cards to take with us on February 6th to Atlanta, Ga to a show.

We will be offering the following menu type items:

coffee
teas
espresso
frappes
smoothies

sandwiches
soups
salads
pastries
ice cream

Our shop is in a rural country-side area and we would like to convey that feel in our shop. In addition to the cafe we will also be selling gifts and furniture and other home decor. Much of this merchandise will be rescued, refurbished or repurposed which is also a core value of what we are all about.

We have a company logo we would like incorporated into the design.

We will also provide files that have the elements of the logo which may also be useful in the design of the card.

Since we are not open yet we need one slightly altered version of the card as well as the final product which states "Opening in the summer 2015"

Target Market(s)

moderate to slightly upscale and folksy.

Industry/Entity Type

Coffee Shop

Contact Information for Business Card

Fern Hollow Coffee
name
address
phone number
email

Card

Font styles to use
Sans Serif

Requirements
Must have
• Must include Logo
• Must include information on menu.
• Must include information on our merchandise sales as described inthe project description.
• Color scheme to complement the logo
Nice to have
• The following descriptions
• "We are also selling gifts, furniture, and other home decoration."
• "We rescue, refurbish, and repurpose old furniture so it can live again."

```html
<!DOCTYPE html>
<html lang="en">
<head>
<meta charset="utf-8">
<title>Fern Hollow Coffee – Business Cards</title>
<link href="https://fonts.googleapis.com/css2?family=Open+Sans:wght@400;600;700&family=Great+Vibes&display=swap" rel="stylesheet">
<style>
  :root {
    --backdrop: #3a302c;
    --paper: #f7f6f4;
    --ink: #3b3b3d;
    --band-dark: #2b2b2e;
    --band-taupe: #a39e8c;
    --maroon: #7a2a33;
    --maroon-text: #7d2630;
    --white: #ffffff;
    --ornament: #ebe7e3;
  }
  * { box-sizing: border-box; margin: 0; padding: 0; }
  html, body { width: 1200px; height: 768px; overflow: hidden; }
  body {
    background: var(--backdrop);
    font-family: "Open Sans", Arial, sans-serif;
    color: var(--ink);
    position: relative;
  }
  .card {
    position: absolute;
    top: 229px;
    width: 540px;
    height: 309px;
    background: var(--paper);
    overflow: hidden;
    box-shadow: 0 8px 24px rgba(0,0,0,.45);
  }
  .card--front { left: 40px; }
  .card--back { left: 620px; }
  .card__waves { position: absolute; inset: 0; width: 100%; height: 100%; }
  .card__ornament {
    position: absolute;
    width: 110px; height: 150px;
    border-radius: 50%;
    background: radial-gradient(ellipse at center, var(--ornament) 0%, rgba(235,231,227,0) 70%);
  }
  .card--front .card__ornament { left: 250px; top: 30px; }
  .card--back .card__ornament { left: 300px; top: 60px; }
  .brand {
    position: absolute;
    display: flex; align-items: center; gap: 10px;
    font-size: 26px; font-weight: 400; color: var(--ink);
    line-height: 1.1;
  }
  .brand__dot { width: 14px; height: 14px; border-radius: 50%; background: var(--maroon); flex: none; }
  .card--front .brand { left: 34px; top: 56px; }
  .card--back .brand { left: 30px; top: 90px; }
  .person { position: absolute; left: 330px; top: 62px; }
  .person__name { font-size: 17px; font-weight: 700; color: var(--maroon-text); }
  .person__role { font-size: 11px; color: var(--ink); margin-top: 2px; }
  .menu {
    position: absolute; right: 26px; top: 218px;
    color: var(--white); font-size: 13px; line-height: 1.45; text-align: right;
    list-style: none;
  }
  .contact {
    position: absolute; right: 22px; top: 88px;
    list-style: none; font-size: 12.5px; line-height: 1.6; text-align: right;
  }
  .contact li { display: flex; justify-content: flex-end; align-items: center; gap: 6px; }
  .contact a { color: inherit; text-decoration: none; }
  .contact .web { color: var(--maroon-text); }
  .icon { width: 13px; height: 13px; flex: none; }
  .opening {
    position: absolute; right: 30px; bottom: 22px;
    font-family: "Great Vibes", cursive; font-size: 27px; color: var(--white);
  }
</style>
</head>
<body>

<section class="card card--front" aria-label="Business card front">
  <svg class="card__waves" viewBox="0 0 540 309" preserveAspectRatio="none" aria-hidden="true">
    <path d="M0,128 C110,170 250,190 540,175 L540,309 L0,309 Z" fill="var(--band-dark)"/>
    <path d="M0,146 C120,185 260,198 540,186 L540,309 L0,309 Z" fill="var(--paper)"/>
    <path d="M0,152 C120,190 260,202 540,190 L540,309 L0,309 Z" fill="var(--band-taupe)"/>
    <path d="M0,158 C120,194 260,206 540,195 L540,309 L0,309 Z" fill="var(--paper)"/>
    <path d="M0,170 C130,206 270,216 540,204 L540,309 L0,309 Z" fill="var(--maroon)"/>
  </svg>
  <div class="card__ornament" role="img" aria-label="Faint floral ornament"></div>
  <div class="brand"><span class="brand__dot"></span>Fern Hollow<br>Coffee</div>
  <div class="person">
    <p class="person__name">Your Long Name</p>
    <p class="person__role">Managing Director</p>
  </div>
  <ul class="menu">
    <li>Coffee « Teas «</li>
    <li>Espresso « Frappes «</li>
    <li>Salads « Sandwiches « Soups «</li>
    <li>Smoothies « Pastries « Ice Cream «</li>
  </ul>
</section>

<section class="card card--back" aria-label="Business card back">
  <svg class="card__waves" viewBox="0 0 540 309" preserveAspectRatio="none" aria-hidden="true">
    <path d="M0,168 C120,215 280,225 540,200 L540,309 L0,309 Z" fill="var(--band-dark)"/>
    <path d="M0,180 C120,222 280,230 540,208 L540,309 L0,309 Z" fill="var(--paper)"/>
    <path d="M0,186 C120,226 280,234 540,213 L540,309 L0,309 Z" fill="var(--band-taupe)"/>
    <path d="M0,192 C120,230 280,238 540,218 L540,309 L0,309 Z" fill="var(--paper)"/>
    <path d="M0,208 C140,242 300,246 540,222 L540,309 L0,309 Z" fill="var(--maroon)"/>
  </svg>
  <div class="card__ornament" role="img" aria-label="Faint floral ornament"></div>
  <div class="brand"><span class="brand__dot"></span>Fern Hollow<br>Coffee</div>
  <ul class="contact">
    <li>Your Commercial or office address
      <svg class="icon" viewBox="0 0 12 12" aria-hidden="true"><path d="M6 1a3.5 3.5 0 0 0-3.5 3.5C2.5 7 6 11 6 11s3.5-4 3.5-6.5A3.5 3.5 0 0 0 6 1z" fill="var(--maroon)"/><circle cx="6" cy="4.5" r="1.3" fill="var(--paper)"/></svg></li>
    <li>00.00.00.0000
      <svg class="icon" viewBox="0 0 12 12" aria-hidden="true"><rect x="1.5" y="4" width="9" height="6" rx="1" fill="var(--maroon)"/><rect x="3.5" y="1.5" width="5" height="3" fill="var(--maroon)"/><rect x="3.5" y="6" width="5" height="2.5" fill="var(--paper)"/></svg>
      00.00.00.0000
      <svg class="icon" viewBox="0 0 12 12" aria-hidden="true"><path d="M2 3.5C2 2 4 1.5 6 1.5S10 2 10 3.5L8.5 5 7.5 4h-3L3.5 5Z M3 6h6l1 4.5H2Z" fill="var(--maroon)"/></svg></li>
    <li><a href="mailto:yourname@yourwebsite.com">yourname@yourwebsite.com</a>
      <svg class="icon" viewBox="0 0 12 12" aria-hidden="true"><rect x="1" y="2.5" width="10" height="7" fill="var(--maroon)"/><path d="M1 2.5l5 4 5-4" stroke="var(--paper)" stroke-width="1" fill="none"/></svg></li>
    <li><a class="web" href="#">www.yourwebsite.com</a>
      <svg class="icon" viewBox="0 0 12 12" aria-hidden="true"><circle cx="6" cy="6" r="5" fill="var(--maroon)"/><path d="M1 6h10M6 1c-2.5 2.5-2.5 7.5 0 10M6 1c2.5 2.5 2.5 7.5 0 10" stroke="var(--paper)" stroke-width=".8" fill="none"/></svg></li>
  </ul>
  <p class="opening">Opening in the summer 2015</p>
</section>

</body>
</html>
```